revised: 'wexford joinery' logo -or- business card

we require a business card or a logo that can be used on a business card & other stationery

(i've just recently decided to open this contest up to logo designs as well - but if you have already been working on a card concept, please feel free to continue with it & submit!)

-

We design and build custom brackets and fixings for our customers and their castles, i.e. homes, offices, workshops, farms etc. Our products might be used to:
- brace or support structures, such as houses, decks, small bridges, etc.
- connect any building material to another
- or could simply be a unique piece that exists as a talking point

As part of our design process we would produce drawings/plans/blue prints/prototypes of the product. Our designs factor in multiple elements, from the materials being joined, the client's taste, and the overall durability demanded by the application - if necessary, the bracket may also be endorsed by a third party, such as a stuctural or mechanical engineer.

The build process takes part in our workshop and on the client's site - some elements may be manufactured off-site, depending on the design chosen and the materials used.

Our brackets are designed to our customers' tastes and could be made to be hidden within the structure or exposed to create interest. Our brackets can be large or small, or be neat with clean lines or take on more of an industrial look.
Updates

please note brief has been updated with a more specific description of our business activity

i have also added the final drawing that was used to water-jet the bracket shown in the photos

also, you will note i changed the title to 'logo + business card'

i don't expect a logo as a discrete artefact of the job, however, i expect that some or all elements on the face of the business card will lend themselves to the street sign (as stated in the original brief) as well as any future logo used on letter heads, invoices, etcetera

another update - changed the allowable entries to include logo's only, as well as business cards

Industry/Entity Type

Industrial

Requirements
Must have
• the face should have the name 'Wexford Joinery' (or no/all-caps)

the number '75' in the logo, which will also be turned into a conservative (residential) street sign ('75' being a street number) - '75' should stand alone -OR- be readily identified by someone who has previously received a business card

i need to make this '75' and any associated 'framing', so it should be transferrable to cad/dxf for machining, laser/water-cutting, brazing/welding, etcet.

(on that note, the winning designer will be able to share their vision for this sign and we'll adhere to it ... within the realms of possibility! if you're happy with the result then you could include it in your portfolio)
Nice to have
• one side of the card needs a majority of space for quotes, hand-written information, etcet. so this side should be white or a light, complimentary colour suitable for black/blue pen

the following should appear somewhere on the card (there is no email or website) :
- name : Mara Quell (Proprietor)
- mobile phone number : +61 (0) 498 716203
- abn: 58 604 917 235

any combination of the following (or equivalent) text:

* 'your castle' - this is slang for your house/place (i prefer this to 'home' as 1: it can apply to a place of business, and 2: for me at least, it conjurs images of wrought iron, brass, hardwood & stone)

* unique

* ...

```html
<!DOCTYPE html>
<html lang="en">
<head>
<meta charset="utf-8">
<title>Wexford Joinery — Business Card</title>
<link href="https://fonts.googleapis.com/css2?family=Arimo:wght@400;700&display=swap" rel="stylesheet">
<style>
  :root {
    --page: #ffffff;
    --ink: #000000;
    --muted: #8a8a8a;
    --card-edge: #cfcfcf;
    --faint: #e4e4e4;
  }
  html, body {
    margin: 0;
    padding: 0;
    width: 847px;
    height: 1200px;
    overflow: hidden;
    background: var(--page);
    font-family: "Arimo", Arial, sans-serif;
    color: var(--ink);
  }
  .canvas {
    position: relative;
    width: 847px;
    height: 1200px;
  }
  .card {
    position: absolute;
    left: 175px;
    width: 494px;
    height: 317px;
    background: var(--page);
    border: 1px solid var(--card-edge);
    box-sizing: border-box;
    overflow: hidden;
  }
  .card--front { top: 248px; }
  .card--back { top: 649px; }
  .card__wedge {
    position: absolute;
    inset: 0;
    width: 100%;
    height: 100%;
  }
  .brand-mark {
    position: absolute;
    left: 45px;
    top: 62px;
    width: 56px;
    height: 56px;
    border: 2px solid var(--page);
    border-radius: 50%;
    box-sizing: border-box;
  }
  .brand-mark__name {
    position: absolute;
    left: 104px;
    top: 72px;
    font-size: 10px;
    font-weight: 700;
    letter-spacing: 0.04em;
    text-transform: uppercase;
    color: var(--ink);
    transform: rotate(-18deg);
    transform-origin: left top;
    display: none;
  }
  .details {
    position: absolute;
    left: 118px;
    top: 150px;
    transform: rotate(-18deg);
    transform-origin: left top;
    white-space: nowrap;
  }
  .details__company {
    margin: 0;
    font-size: 22px;
    font-weight: 700;
    letter-spacing: -0.01em;
    line-height: 1;
  }
  .details__tagline {
    margin: 4px 0 0;
    font-size: 11px;
    color: var(--muted);
  }
  .details__person {
    margin: 22px 0 0 8px;
    font-size: 17px;
  }
  .details__role {
    font-size: 11px;
  }
  .details__contact {
    margin: 18px 0 0 14px;
    font-size: 12px;
    line-height: 1.35;
  }
  .faint-mark {
    position: absolute;
    left: 187px;
    top: 37px;
    width: 236px;
    height: 236px;
    border: 3px solid var(--faint);
    border-radius: 50%;
    box-sizing: border-box;
    display: flex;
    align-items: center;
    justify-content: center;
  }
  .faint-mark__name {
    font-size: 22px;
    font-weight: 700;
    color: var(--faint);
  }
</style>
</head>
<body>
<main class="canvas">

  <section class="card card--front" aria-label="Business card front">
    <svg class="card__wedge" viewBox="0 0 494 317" preserveAspectRatio="none" aria-hidden="true">
      <polygon points="0,0 58,0 100,317 0,317" fill="var(--ink)"/>
    </svg>
    <div class="brand-mark" aria-hidden="true"></div>
    <div class="details">
      <h1 class="details__company">Wexford Joinery</h1>
      <p class="details__tagline">Bespoke Bracket Manufacturing Service</p>
      <p class="details__person">Mara Quell <span class="details__role">(Proprietor)</span></p>
      <p class="details__contact">Mobile : +61 (0) 498 716203<br>Abn: 58 604 917 235</p>
    </div>
  </section>

  <section class="card card--back" aria-label="Business card back">
    <svg class="card__wedge" viewBox="0 0 494 317" preserveAspectRatio="none" aria-hidden="true">
      <polygon points="0,0 22,0 104,317 0,317" fill="var(--ink)"/>
    </svg>
    <div class="faint-mark">
      <span class="faint-mark__name">Wexford Joinery</span>
    </div>
  </section>

</main>
</body>
</html>
```